Rocket business card

Modern business card design, use of color is good with clean space too.

Things to include on card:

Quote: I add fuel to your optometry practice

- Eyewear Sales
- Admin Duties
- Revenue Collection
- Leadership
- Tech Adoption
- COGS Reduction
- Product Sourcing
-Medical Growth

Dalton Vesk, CEO
Lume Vantor
Text Me! 847-302-6194
dalton@lumevantor.net

```html
<!DOCTYPE html>
<html lang="en">
<head>
<meta charset="utf-8">
<title>Lume Vantor – Business Card</title>
<link href="https://fonts.googleapis.com/css2?family=Montserrat:wght@500;700&family=Roboto:wght@400;500&display=swap" rel="stylesheet">
<style>
  :root {
    --backdrop: #2b2b2d;
    --card: #161616;
    --card-warm: #1b1513;
    --ink: #f4f4f4;
    --orange: #f39a1e;
    --red-orange: #e3462a;
    --glow: #2a1a14;
  }
  * { margin: 0; padding: 0; box-sizing: border-box; }
  html, body { width: 1200px; height: 874px; overflow: hidden; }
  body {
    background: var(--backdrop);
    position: relative;
    font-family: "Roboto", sans-serif;
    color: var(--ink);
  }
  .card {
    position: absolute;
    width: 580px;
    height: 330px;
    background: var(--card);
    box-shadow: 0 14px 30px rgba(0,0,0,.45);
    overflow: hidden;
  }

  /* Back side */
  .card-back { left: 390px; top: 70px; }
  .brand-lockup {
    position: absolute;
    left: 0; right: 0; top: 92px;
    display: flex; align-items: center; justify-content: center; gap: 16px;
  }
  .brand-dot {
    width: 40px; height: 40px; border-radius: 50%;
    background: linear-gradient(135deg, var(--red-orange), var(--orange));
  }
  .brand-name {
    font-family: "Montserrat", sans-serif;
    font-weight: 500;
    font-size: 38px;
    letter-spacing: 2px;
    color: var(--ink);
  }
  .services {
    position: absolute;
    left: 0; right: 0; top: 196px;
    text-align: center;
    font-size: 15px;
    line-height: 21px;
  }
  .services .sep { color: var(--orange); margin: 0 6px; }

  /* Front side */
  .card-front { left: 230px; top: 470px; background: var(--card); }
  .decor-glow {
    position: absolute;
    left: -40px; top: -30px;
    width: 400px; height: 400px; border-radius: 50%;
    background: var(--glow);
    opacity: .8;
  }
  .person {
    position: absolute; left: 40px; top: 112px;
  }
  .person-name {
    font-family: "Montserrat", sans-serif;
    font-weight: 700;
    font-size: 26px;
    color: var(--orange);
    text-transform: uppercase;
  }
  .person-role {
    font-family: "Montserrat", sans-serif;
    font-weight: 500;
    font-size: 19px;
    margin-top: 2px;
  }
  .rule {
    position: absolute; left: 40px; top: 188px;
    display: flex; height: 4px;
  }
  .rule span { display: block; height: 4px; }
  .rule .white { width: 170px; background: var(--ink); }
  .rule .heat { width: 200px; background: linear-gradient(90deg, var(--red-orange), var(--orange), var(--red-orange)); }
  .rule .white-end { width: 160px; background: var(--ink); }
  .contacts {
    position: absolute; left: 40px; top: 206px;
    list-style: none;
    font-size: 16px; line-height: 26px;
  }
  .contacts li { display: flex; align-items: center; gap: 10px; }
  .contacts svg { width: 16px; height: 16px; fill: var(--orange); }
  .front-brand {
    position: absolute; right: 48px; top: 84px;
    display: flex; align-items: center; gap: 12px;
  }
  .front-brand .brand-dot { width: 28px; height: 28px; }
  .front-brand .brand-name { font-size: 30px; letter-spacing: 1px; }
  .website {
    position: absolute; right: 48px; bottom: 22px;
    font-size: 17px; letter-spacing: 2px;
  }
  .website .domain { color: var(--orange); }
</style>
</head>
<body>

  <section class="card card-back" aria-label="Card back">
    <div class="brand-lockup">
      <span class="brand-dot"></span>
      <span class="brand-name">LUME VANTOR</span>
    </div>
    <p class="services">
      Eyewear Sales<span class="sep">•</span>Admin Duties<span class="sep">•</span>Revenue Collection<br>
      Leadership<span class="sep">•</span>Tech Adoption<span class="sep">•</span>COGS Reduction<br>
      Product Sourcing<span class="sep">•</span>Medical Growth
    </p>
  </section>

  <section class="card card-front" aria-label="Card front">
    <div class="decor-glow" role="img" aria-label="Faint warm background glow"></div>

    <div class="person">
      <h1 class="person-name">Dalton Vesk</h1>
      <p class="person-role">CEO</p>
    </div>

    <div class="rule"><span class="white"></span><span class="heat"></span><span class="white-end"></span></div>

    <ul class="contacts">
      <li>
        <svg viewBox="0 0 24 24" aria-hidden="true"><path d="M6.6 10.8a15.2 15.2 0 0 0 6.6 6.6l2.2-2.2a1 1 0 0 1 1-.25 11.4 11.4 0 0 0 3.6.57 1 1 0 0 1 1 1V20a1 1 0 0 1-1 1A17 17 0 0 1 3 4a1 1 0 0 1 1-1h3.5a1 1 0 0 1 1 1c0 1.25.2 2.45.57 3.57a1 1 0 0 1-.25 1z"/></svg>
        847-302-6194 (Text Me!)
      </li>
      <li>
        <svg viewBox="0 0 24 24" aria-hidden="true"><path d="M2 5h20v14H2z" opacity=".9"/><path d="M2 5l10 8 10-8" fill="none" stroke="#161616" stroke-width="2"/></svg>
        dalton@lumevantor.net
      </li>
    </ul>

    <div class="front-brand">
      <span class="brand-dot"></span>
      <span class="brand-name">LUME VANTOR</span>
    </div>

    <p class="website">www.<span class="domain">lumevantor</span>.net</p>
  </section>

</body>
</html>
```